Working Capital graphics

Our business advisory firm requires 9 images to be re-created and improved in the branding of our business.

The 9 images have been uploaded below and the colours and branding of the business can be found at the website www.thornwickadvisory.com.au

```html
<!DOCTYPE html>
<html lang="en">
<head>
<meta charset="utf-8">
<title>Working Capital</title>
<link rel="stylesheet" href="https://fonts.googleapis.com/css2?family=Open+Sans:wght@700;800&display=swap">
<style>
  :root {
    --navy: #0f3a86;
    --sky: #0db1f2;
    --orange: #f7941d;
    --label: #2e3192;
    --white: #ffffff;
  }
  html, body {
    margin: 0;
    padding: 0;
    width: 1200px;
    height: 1000px;
    overflow: hidden;
    background: var(--white);
  }
  .diagram {
    display: block;
    width: 1200px;
    height: 1000px;
  }
  .hub-ring { fill: none; stroke: var(--navy); stroke-width: 14; }
  .hub-core { fill: var(--sky); }
  .hub-title {
    font-family: "Open Sans", Arial, sans-serif;
    font-weight: 800;
    font-size: 60px;
    fill: var(--white);
    text-anchor: middle;
  }
  .spoke { stroke: var(--navy); stroke-width: 14; }
  .joint { fill: var(--white); stroke: var(--navy); stroke-width: 7; }
  .node-fill { fill: var(--white); }
  .node-arc { fill: none; stroke-width: 13; }
  .node-arc--warm { stroke: var(--orange); }
  .node-arc--cool { stroke: var(--sky); }
  .node-label {
    font-family: "Open Sans", Arial, sans-serif;
    font-weight: 700;
    font-size: 28px;
    fill: var(--label);
    text-anchor: middle;
  }
</style>
</head>
<body>
<svg class="diagram" viewBox="0 0 1800 1500" xmlns="http://www.w3.org/2000/svg" aria-label="Working capital drivers">
  <defs>
    <g id="node">
      <circle class="node-fill" r="122"/>
      <path class="node-arc node-arc--warm" d="M0 -122 A122 122 0 0 0 0 122"/>
      <path class="node-arc node-arc--cool" d="M0 -122 A122 122 0 0 1 0 122"/>
    </g>
  </defs>

  <!-- spokes -->
  <g class="spokes">
    <line class="spoke" x1="890" y1="459" x2="892" y2="273"/>
    <line class="spoke" x1="1086" y1="534" x2="1210" y2="388"/>
    <line class="spoke" x1="1175" y1="712" x2="1370" y2="703"/>
    <line class="spoke" x1="1124" y1="932" x2="1296" y2="1020"/>
    <line class="spoke" x1="984" y1="1034" x2="1030" y2="1220"/>
    <line class="spoke" x1="776" y1="1022" x2="696" y2="1198"/>
    <line class="spoke" x1="628" y1="891" x2="453" y2="973"/>
    <line class="spoke" x1="598" y1="683" x2="413" y2="663"/>
    <line class="spoke" x1="697" y1="519" x2="563" y2="380"/>
  </g>

  <!-- hub -->
  <circle class="hub-ring" cx="883" cy="753" r="292"/>
  <circle class="hub-core" cx="883" cy="753" r="240"/>
  <text class="hub-title" x="890" y="742">WORKING</text>
  <text class="hub-title" x="890" y="812">CAPITAL</text>

  <!-- joints -->
  <g class="joints">
    <circle class="joint" cx="890" cy="459" r="12"/>
    <circle class="joint" cx="1086" cy="534" r="12"/>
    <circle class="joint" cx="1175" cy="712" r="12"/>
    <circle class="joint" cx="1124" cy="932" r="12"/>
    <circle class="joint" cx="984" cy="1034" r="12"/>
    <circle class="joint" cx="776" cy="1022" r="12"/>
    <circle class="joint" cx="628" cy="891" r="12"/>
    <circle class="joint" cx="598" cy="683" r="12"/>
    <circle class="joint" cx="697" cy="519" r="12"/>
  </g>

  <!-- nodes -->
  <g class="node" transform="translate(892 273)">
    <use href="#node"/>
    <text class="node-label" y="-34">Supply</text>
    <text class="node-label" y="13">Chain</text>
    <text class="node-label" y="60">Issues</text>
  </g>
  <g class="node" transform="translate(1210 388)">
    <use href="#node"/>
    <text class="node-label" y="-8">Process</text>
    <text class="node-label" y="39">Issues</text>
  </g>
  <g class="node" transform="translate(1370 703)">
    <use href="#node"/>
    <text class="node-label" y="-12">Forecasting</text>
    <text class="node-label" y="35">and Planning</text>
  </g>
  <g class="node" transform="translate(1296 1020)">
    <use href="#node"/>
    <text class="node-label" y="-14">Customer</text>
    <text class="node-label" y="33">Management</text>
  </g>
  <g class="node" transform="translate(1030 1220)">
    <use href="#node"/>
    <text class="node-label" y="-11">SKU</text>
    <text class="node-label" y="36">Complexity</text>
  </g>
  <g class="node" transform="translate(696 1198)">
    <use href="#node"/>
    <text class="node-label" y="-11">Supplier</text>
    <text class="node-label" y="36">Management</text>
  </g>
  <g class="node" transform="translate(453 973)">
    <use href="#node"/>
    <text class="node-label" y="-10">KPIs and</text>
    <text class="node-label" y="37">Measures</text>
  </g>
  <g class="node" transform="translate(413 663)">
    <use href="#node"/>
    <text class="node-label" y="-33">IT Systems</text>
    <text class="node-label" y="14">and</text>
    <text class="node-label" y="61">Information</text>
  </g>
  <g class="node" transform="translate(563 380)">
    <use href="#node"/>
    <text class="node-label" y="-17">Terms and</text>
    <text class="node-label" y="30">Conditions</text>
  </g>
</svg>
</body>
</html>
```